QTVlink PowerPoint Template with existing Logo and Letterhead template

Develop a PowerPoint template based on existing logo and letterhead designs for a Marketing Consultancy.
Presentations that will be made with title slide, content slides (which includes mostly bullet point text and some tables) and also last page company introduction and copyright.
Corporate colors should be keep as per the logo

I like something like from Pixel Harbor
- Serious, Modern PowerPoint Design for Company in Canada | Design 418674
- Professional, Modern PowerPoint Design for Company in United States | Design 7795293
- Professional, Modern PowerPoint Design for Company in United States | Design 7826742
- Serious, Modern PowerPoint Design for Company in Canada | Design 418635
- Elegant, Serious PowerPoint Design for Company in Puerto Rico | Design 16951178
- Bold, Modern PowerPoint Design for Company in United States | Design 11745238

To all designers, • We need sleek and modern looking PowerPoint presentation template. • The template will primarily be used for our corporate slide and solutions presentation for our customers. • Not too much of white and it should be sleek, modern and impressive for marketing consultancy firms like us. • Please ensure the content pages are water marketed with the 4 boxes. • I like something like from Pixel Harbor and you can get some idea on what I like.: o Serious, Modern PowerPoint Design for Company in Canada | Design 418674 o Professional, Modern PowerPoint Design for Company in United States | Design 7795293 o Professional, Modern PowerPoint Design for Company in United States | Design 7826742 o Serious, Modern PowerPoint Design for Company in Canada | Design 418635 o Elegant, Serious PowerPoint Design for Company in Puerto Rico | Design 16951178 o Bold, Modern PowerPoint Design for Company in United States | Design 11745238 Thanks!

Target Market(s)

Marketing Managers, B2B Marketing Team, CRM Data Owners

Industry/Entity Type

Marketing

Requirements
Must have
• Not too much of white and it should be sleek, modern and impressive for marketing consultancy firms like us. Please ensure the content pages are water marketed with the 4 boxes. The template will primarily be used for our corporate slides and solutions presentation for our customers.
Should not have
• no background in the slide content area

```html
<!DOCTYPE html>
<html lang="en">
<head>
<meta charset="utf-8">
<title>QTVlink Presentation Template</title>
<link href="https://fonts.googleapis.com/css2?family=Open+Sans:wght@400;600;700;800&display=swap" rel="stylesheet">
<style>
:root{
  --red:#e31e26;
  --slate:#4a5263;
  --slate-dark:#363c49;
  --ink:#333640;
  --muted:#8a8e96;
  --rule:#e6e6e6;
  --ghost:#f6f6f7;
  --cell:#f0f0f0;
}
*{box-sizing:border-box;margin:0;padding:0}
html,body{width:1200px;height:1200px;overflow:hidden;background:#fff}
body{position:relative;font-family:"Open Sans",Arial,sans-serif;color:var(--ink)}
.slide{position:absolute;width:472px;height:266px;background:#fff;overflow:hidden;
  box-shadow:0 0 0 1px #eee,0 2px 6px rgba(0,0,0,.12)}
.col-l{left:110px}.col-r{left:619px}
.row-1{top:34px}.row-2{top:323px}.row-3{top:612px}.row-4{top:901px}

.accent{position:absolute;left:18px;top:0;width:60px;height:2px;background:var(--red)}
.topic{position:absolute;left:22px;top:17px;font-size:5.5px;color:var(--muted)}
.title{position:absolute;left:22px;top:23px;font-size:13px;font-weight:700;color:var(--red);letter-spacing:-.1px}
.brand{position:absolute;right:20px;top:24px;font-size:10px;font-weight:800;color:var(--red);display:flex;align-items:center;gap:3px}
.brand i{display:block;width:4px;height:4px;background:var(--slate)}
.divider{position:absolute;left:18px;right:18px;top:47px;height:1px;background:var(--rule)}
.footer{position:absolute;right:10px;bottom:5px;font-size:4px;color:#bbb;padding:3px 6px 2px 16px;border-top:1px solid #eee;border-left:1px solid #eee}

.watermark{position:absolute;right:0;top:50px;width:140px;height:210px;pointer-events:none}
.watermark span{position:absolute;background:var(--ghost)}
.watermark span:nth-child(1){left:60px;top:0;width:30px;height:30px}
.watermark span:nth-child(2){left:92px;top:36px;width:40px;height:40px}
.watermark span:nth-child(3){left:36px;top:44px;width:48px;height:48px}
.watermark span:nth-child(4){left:70px;top:100px;width:66px;height:66px}

.body-text{font-size:6.6px;line-height:10.2px;color:var(--ink)}
.body-text p{margin-bottom:5px}
.two-col{position:absolute;top:66px;left:22px;right:22px;display:flex;gap:18px}
.two-col>div{flex:1}

.bullets{position:absolute;top:66px;left:26px;right:30px;list-style:none}
.bullets li{position:relative;padding-left:10px;margin-bottom:5px}
.bullets li::before{content:"›";position:absolute;left:0;top:0;color:var(--ink)}
.bullets li.gap{margin-top:14px}

.fin-caption{position:absolute;left:38px;top:69px;font-size:7.5px;color:var(--ink)}
table{border-collapse:collapse}
.fin{position:absolute;left:35px;top:84px;width:401px;font-size:6.3px}
.fin th{background:var(--red);color:#fff;font-weight:700;height:17px;width:53px;border-right:1px solid #f57a7f}
.fin th.blank{background:transparent;width:83px;border:none}
.fin td{height:13.6px;text-align:center;border-bottom:1px solid #ddd;border-right:1px solid var(--red)}
.fin td:first-child{text-align:left;padding-left:4px;border-right:none}
.fin tr.total td{background:#e4e4e4;font-weight:700;font-size:7.2px;height:15px;border-bottom:none}

.steps{position:absolute;left:34px;top:86px}
.step-label{font-size:7.2px;font-weight:700}
.step-copy{font-size:6px}

.months{position:absolute;left:0;top:0;width:100%;height:100%}
.month{position:absolute;width:92px}
.pill{display:inline-block;width:37px;height:14px;border-radius:7px;background:var(--red);color:#fff;font-size:5.5px;font-weight:700;text-align:center;line-height:14px}
.month h4{font-size:7.4px;font-weight:400;color:var(--red);margin:5px 0 4px 1px}
.month p{font-size:5.6px;line-height:7.6px;color:var(--ink);padding-left:1px}

.options{position:absolute;left:19px;top:69px;width:434px;font-size:6px}
.options th{background:var(--red);color:#fff;font-weight:700;height:22px;width:54px;border-right:1px solid #f57a7f}
.options td{height:23px;text-align:center;border-bottom:1px solid #ececec;border-right:1px solid #ececec;color:var(--ink)}
.options td:first-child{color:var(--muted);text-align:left;padding-left:13px}

.features{position:absolute;left:30px;top:67px;list-style:none}
.features li{display:flex;align-items:center;gap:10px;height:34px}
.features svg{flex:none}
.features strong{display:block;font-size:7.6px;font-weight:700;color:var(--ink)}
.features span{display:block;font-size:5.6px;color:var(--muted)}

.closing-photo{position:absolute;left:36px;top:0;width:181px;height:266px;background:linear-gradient(160deg,#eef1f5 0%,#f7f8fa 55%,#e9ecf0 100%)}
.closing-panel{position:absolute;left:36px;top:0;width:181px;height:266px;text-align:center}
.closing-brand{position:absolute;top:66px;width:100%;font-size:14px;font-weight:800;color:var(--red);display:flex;justify-content:center;align-items:center;gap:4px}
.closing-brand i{display:block;width:5px;height:5px;background:var(--slate)}
.thanks{position:absolute;top:116px;width:100%;font-size:22px;font-weight:800;color:var(--red)}
.thanks-sub{position:absolute;top:144px;width:100%;font-size:7px;font-weight:700;color:var(--slate-dark)}
.contact{position:absolute;left:35px;top:165px;font-size:7.4px;font-weight:600;color:var(--slate-dark);line-height:16px;text-align:left}
.contact b{color:var(--red);display:inline-block;width:12px}
.fine{position:absolute;top:246px;left:36px;right:36px;font-size:3.8px;color:var(--muted);line-height:5px}
.sq{position:absolute}
.sq.red{background:var(--red)}
.sq.slate{background:var(--slate)}
</style>
</head>
<body>

<!-- Two-column text -->
<section class="slide col-l row-1">
  <div class="watermark"><span></span><span></span><span></span><span></span></div>
  <div class="accent"></div><div class="topic">Main topic here</div><div class="title">Slide title here</div>
  <div class="brand">QTVlink<i></i></div><div class="divider"></div>
  <div class="two-col body-text">
    <div>
      <p>Lorem ipsum dolor sit amet, nam graece verear apeirian ut. Duo cu alii definitionem, magna accumsan quo at. Id quo illum option mediocritatem, et illud simul nam, at vel nibh docendi posidonium. Mei ei tation evertitur.</p>
      <p>Cum et probo sadipscing, in duo illum pertinacia. Sea ea ullum sapientem. Aeque interpretaris et pro, nec lucilius repudiandae id. Vim ea nobis vitae, id nisl melius ius. Ne wisi persecuti his. Justo erant movet cu eam.</p>
      <p>Per vero vidit disputando an, no case reprimique eam, et tritani accommodare vim. Ut vis mandamus reformidans, vidit latine neglegentur at cum. Ut malis error eam. His eu quot verear, facilis voluptaria eu mea. Vix vide fugit omittantur et. Has ut habeo volumus argumentum. Duo id offendit atomorum.</p>
    </div>
    <div>
      <p>Cum tempor integre honestatis in, et sit hinc graeco vocibus. Has id graecis appetere mnesarchum. Ei error convenire iracundia cum, nec ne putant utroque. Cum id quem liberavisse theophrastus, at unum nostrud aliquando eam. Ea utamur splendide vel. Prima aeque duo ad, vel an quando sensibus deterruisset.</p>
      <p>Et mel congue vidisse. Id ubique impedit argumentum pri, ne ignota nostrum cum. Legimus accusata patrioque eu mel, ei vel alia placerat, quo harum cetero dignissim an. Cum no augue choro, has clita ceteros tibique no. Alia graece scripserit id vis. Dicunt signiferumque duo in, eum regione bonorum alienum et, duis mazim est an.</p>
    </div>
  </div>
  <div class="footer">qtvlink.example | 7</div>
</section>

<!-- Bullets -->
<section class="slide col-r row-1">
  <div class="watermark"><span></span><span></span><span></span><span></span></div>
  <div class="accent"></div><div class="topic">Main topic here</div><div class="title">Slide title here</div>
  <div class="brand">QTVlink<i></i></div><div class="divider"></div>
  <ul class="bullets body-text">
    <li>Lorem ipsum dolor sit amet, nam graece verear apeirian ut. Duo cu alii definitionem, magna accumsan quo at. Id quo illum option mediocritatem, et illud simul nam, at vel nibh docendi posidonium. Mei ei tation evertitur.</li>
    <li>Cum et probo sadipscing, in duo illum pertinacia. Sea ea ullum sapientem. Aeque interpretaris et pro, nec lucilius repudiandae id. Vim ea nobis vitae, id nisl melius ius. Ne wisi persecuti his. Justo erant movet cu eam.</li>
    <li>Per vero vidit disputando an, no case reprimique eam, et tritani accommodare vim. Ut vis mandamus reformidans, vidit latine neglegentur at cum. Ut malis error eam. His eu quot verear, facilis voluptaria eu mea. Vix vide fugit omittantur et. Has ut habeo volumus argumentum. Duo id offendit atomorum.</li>
    <li class="gap">Cum tempor integre honestatis in, et sit hinc graeco vocibus. Has id graecis appetere mnesarchum. Ei error convenire iracundia cum, nec ne putant utroque. Cum id quem liberavisse theophrastus, at unum nostrud aliquando eam. Ea utamur splendide vel. Prima aeque duo ad, vel an quando sensibus deterruisset.</li>
    <li>Et mel congue vidisse. Id ubique impedit argumentum pri, ne ignota nostrum cum. Legimus accusata patrioque eu mel, ei vel alia placerat, quo harum cetero dignissim an. Cum no augue choro, has clita ceteros tibique no. Alia graece scripserit id vis. Dicunt signiferumque duo in, eum regione bonorum alienum et, duis mazim est an.</li>
  </ul>
  <div class="footer">qtvlink.example | 8</div>
</section>

<!-- Financial table -->
<section class="slide col-l row-2">
  <div class="watermark"><span></span><span></span><span></span><span></span></div>
  <div class="accent"></div><div class="topic">Main topic here</div><div class="title">Slide title here</div>
  <div class="brand">QTVlink<i></i></div><div class="divider"></div>
  <div class="fin-caption">Financials (billions)</div>
  <table class="fin">
    <tr><th class="blank"></th><th>2010</th><th>2011</th><th>2012</th><th>2013</th><th>2014</th><th>2015</th></tr>
    <tr><td>Revenue</td><td>15.6</td><td>17.1</td><td>15.6</td><td>17.1</td><td>15.6</td><td>17.1</td></tr>
    <tr><td>Cost of Revenue</td><td>10.6</td><td>10.8</td><td>10.6</td><td>10.8</td><td>10.6</td><td>10.8</td></tr>
    <tr><td>Gross Profit</td><td>5.0</td><td>6.3</td><td>5.0</td><td>6.3</td><td>5.0</td><td>6.3</td></tr>
    <tr><td>R&amp;D</td><td>0.48</td><td>0.49</td><td>0.48</td><td>0.49</td><td>0.48</td><td>0.49</td></tr>
    <tr><td>General/Sales</td><td>1.1</td><td>1.0</td><td>1.1</td><td>1.0</td><td>1.1</td><td>1.0</td></tr>
    <tr><td>EBITDA</td><td>3.4</td><td>4.8</td><td>3.4</td><td>4.8</td><td>3.4</td><td>4.8</td></tr>
    <tr><td>Tax</td><td>1.3</td><td>1.9</td><td>1.3</td><td>1.9</td><td>1.3</td><td>1.9</td></tr>
    <tr><td>Interest Expense</td><td>–</td><td>–</td><td>–</td><td>–</td><td>–</td><td>–</td></tr>
    <tr class="total"><td>Net Income</td><td>2.1</td><td>2.9</td><td>2.1</td><td>2.9</td><td>2.1</td><td>2.9</td></tr>
  </table>
  <div class="footer">qtvlink.example | 12</div>
</section>

<!-- Process steps -->
<section class="slide col-r row-2">
  <div class="watermark"><span></span><span></span><span></span><span></span></div>
  <div class="accent"></div><div class="topic">Main topic here</div><div class="title">Slide title here</div>
  <div class="brand">QTVlink<i></i></div><div class="divider"></div>
  <svg class="steps" width="410" height="118" viewBox="0 0 410 118">
    <defs>
      <linearGradient id="gRed" x1="0" x2="1"><stop offset="0" stop-color="#f0252d"/><stop offset="1" stop-color="#c9161d"/></linearGradient>
      <linearGradient id="gSlate" x1="0" x2="1"><stop offset="0" stop-color="#525a6b"/><stop offset="1" stop-color="#343a46"/></linearGradient>
      <path id="chev" d="M4,0 H70 Q76,0 80,6 L104,52 Q107,58 104,64 L80,110 Q76,116 70,116 H4 L14,104 H62 Q68,104 71,98 L88,64 Q91,58 88,52 L71,18 Q68,12 62,12 H14 Z"/>
    </defs>
    <g><use href="#chev" fill="url(#gRed)"/>
      <text x="13" y="43" class="step-label" fill="#e31e26">Step 1</text>
      <text class="step-copy" fill="#222"><tspan x="13" y="58">Lorem ipsum</tspan><tspan x="13" y="66">dolor sit amet,</tspan><tspan x="13" y="74">consectetur</tspan><tspan x="13" y="82">adipiscised do</tspan><tspan x="13" y="90">dolore magna</tspan><tspan x="13" y="98">aliqua.</tspan></text></g>
    <g transform="translate(100,0)"><use href="#chev" fill="url(#gSlate)"/>
      <text x="13" y="43" class="step-label" fill="#363c49">Step 2</text>
      <text class="step-copy" fill="#222"><tspan x="13" y="58">Lorem ipsum</tspan><tspan x="13" y="66">dolor sit amet,</tspan><tspan x="13" y="74">consectetur</tspan><tspan x="13" y="82">adipiscised do</tspan><tspan x="13" y="90">dolore magna</tspan><tspan x="13" y="98">aliqua.</tspan></text></g>
    <g transform="translate(200,0)"><use href="#chev" fill="url(#gRed)"/>
      <text x="13" y="43" class="step-label" fill="#e31e26">Step 3</text>
      <text class="step-copy" fill="#222"><tspan x="13" y="58">Lorem ipsum</tspan><tspan x="13" y="66">dolor sit amet,</tspan><tspan x="13" y="74">consectetur</tspan><tspan x="13" y="82">adipiscised do</tspan><tspan x="13" y="90">dolore magna</tspan><tspan x="13" y="98">aliqua.</tspan></text></g>
    <g transform="translate(300,0)"><use href="#chev" fill="url(#gSlate)"/>
      <text x="13" y="43" class="step-label" fill="#363c49">Step 4</text>
      <text class="step-copy" fill="#222"><tspan x="13" y="58">Lorem ipsum</tspan><tspan x="13" y="66">dolor sit amet,</tspan><tspan x="13" y="74">consectetur</tspan><tspan x="13" y="82">adipiscised do</tspan><tspan x="13" y="90">dolore magna</tspan><tspan x="13" y="98">aliqua.</tspan></text></g>
  </svg>
  <div class="footer">qtvlink.example | 11</div>
</section>

<!-- Timeline months -->
<section class="slide col-l row-3">
  <div class="watermark"><span></span><span></span><span></span><span></span></div>
  <div class="accent"></div><div class="topic">Main topic here</div><div class="title">Slide title here</div>
  <div class="brand">QTVlink<i></i></div><div class="divider"></div>
  <div class="months">
    <div class="month" style="left:33px;top:69px"><span class="pill">JAN</span><h4>Title text demo</h4><p>Lorem ipsum dolor sit amet, consectetur adipiscing elit, incididunt ut labore et dolore magna veniam, quis nostrud</p></div>
    <div class="month" style="left:138px;top:69px"><span class="pill">FEB</span><h4>Title text demo</h4><p>Lorem ipsum dolor sit amet, consectetur adipiscing elit, incididunt ut labore et dolore magna veniam, quis nostrud</p></div>
    <div class="month" style="left:244px;top:69px"><span class="pill">MAY</span><h4>Title text demo</h4><p>Lorem ipsum dolor sit amet, consectetur adipiscing elit, incididunt ut labore et dolore magna veniam, quis nostrud</p></div>
    <div class="month" style="left:350px;top:69px"><span class="pill">JUN</span><h4>Title text demo</h4><p>Lorem ipsum dolor sit amet, consectetur adipiscing elit, incididunt ut labore et dolore magna veniam, quis nostrud</p></div>
    <div class="month" style="left:33px;top:155px"><span class="pill">JUL</span><h4>Title text demo</h4><p>Lorem ipsum dolor sit amet, consectetur adipiscing elit, incididunt ut labore et dolore magna veniam, quis nostrud</p></div>
    <div class="month" style="left:138px;top:155px"><span class="pill">AUG</span><h4>Title text demo</h4><p>Lorem ipsum dolor sit amet, consectetur adipiscing elit, incididunt ut labore et dolore magna veniam, quis nostrud</p></div>
    <div class="month" style="left:244px;top:155px"><span class="pill">SEP</span><h4>Title text demo</h4><p>Lorem ipsum dolor sit amet, consectetur adipiscing elit, incididunt ut labore et dolore magna veniam, quis nostrud</p></div>
    <div class="month" style="left:350px;top:155px"><span class="pill">NOV</span><h4>Title text demo</h4><p>Lorem ipsum dolor sit amet, consectetur adipiscing elit, incididunt ut labore et dolore magna veniam, quis nostrud</p></div>
  </div>
  <div class="footer">qtvlink.example | 13</div>
</section>

<!-- Options pricing table -->
<section class="slide col-r row-3">
  <div class="watermark"><span></span><span></span><span></span><span></span></div>
  <div class="accent"></div><div class="topic">Main topic here</div><div class="title">Slide title here</div>
  <div class="brand">QTVlink<i></i></div><div class="divider"></div>
  <table class="options">
    <tr><th></th><th>Option 01</th><th>Option 02</th><th>Option 03</th><th>Option 04</th><th>Option 05</th><th>Option 06</th><th>Option 07</th></tr>
    <tr><td>Option 01</td><td>$32,500</td><td>$32,500</td><td>$32,500</td><td>$32,500</td><td>$32,500</td><td>$32,500</td><td>$32,500</td></tr>
    <tr><td>Option 02</td><td>$32,500</td><td>$32,500</td><td>$32,500</td><td>$32,500</td><td>$32,500</td><td>$32,500</td><td>$32,500</td></tr>
    <tr><td>Option 03</td><td>$32,500</td><td>$32,500</td><td>$32,500</td><td>$32,500</td><td>$32,500</td><td>$32,500</td><td>$32,500</td></tr>
    <tr><td>Option 04</td><td>$32,500</td><td>$32,500</td><td>$32,500</td><td>$32,500</td><td>$32,500</td><td>$32,500</td><td>$32,500</td></tr>
    <tr><td>Option 05</td><td>$32,500</td><td>$32,500</td><td>$32,500</td><td>$32,500</td><td>$32,500</td><td>$32,500</td><td>$32,500</td></tr>
    <tr><td>Option 06</td><td>$32,500</td><td>$32,500</td><td>$32,500</td><td>$32,500</td><td>$32,500</td><td>$32,500</td><td>$32,500</td></tr>
  </table>
  <div class="footer">qtvlink.example | 9</div>
</section>

<!-- Features list -->
<section class="slide col-l row-4">
  <div class="watermark"><span></span><span></span><span></span><span></span></div>
  <div class="accent"></div><div class="topic">Main topic here</div><div class="title">Slide title here</div>
  <div class="brand">QTVlink<i></i></div><div class="divider"></div>
  <ul class="features">
    <li><svg width="20" height="20" viewBox="0 0 20 20"><circle cx="10" cy="10" r="9" fill="none" stroke="#e31e26" stroke-width="1.2"/><path d="M6 10.2 L9 13 L14.5 6.5" fill="none" stroke="#e31e26" stroke-width="1.2"/></svg><div><strong>Feature #1</strong><span>Lorem ipsum dolor sit amet, ex paulo vidisse eos. Nec ut persius admodum civibus, an hinc iudico principes sea.</span></div></li>
    <li><svg width="20" height="20" viewBox="0 0 20 20"><circle cx="10" cy="10" r="9" fill="none" stroke="#e31e26" stroke-width="1.2"/><path d="M6 10.2 L9 13 L14.5 6.5" fill="none" stroke="#e31e26" stroke-width="1.2"/></svg><div><strong>Feature #2</strong><span>Lorem ipsum dolor sit amet, ex paulo vidisse eos. Nec ut persius admodum civibus, an hinc iudico principes sea.</span></div></li>
    <li><svg width="20" height="20" viewBox="0 0 20 20"><circle cx="10" cy="10" r="9" fill="none" stroke="#e31e26" stroke-width="1.2"/><path d="M6 10.2 L9 13 L14.5 6.5" fill="none" stroke="#e31e26" stroke-width="1.2"/></svg><div><strong>Feature #3</strong><span>Lorem ipsum dolor sit amet, ex paulo vidisse eos. Nec ut persius admodum civibus, an hinc iudico principes sea.</span></div></li>
    <li><svg width="20" height="20" viewBox="0 0 20 20"><circle cx="10" cy="10" r="9" fill="none" stroke="#e31e26" stroke-width="1.2"/><path d="M6 10.2 L9 13 L14.5 6.5" fill="none" stroke="#e31e26" stroke-width="1.2"/></svg><div><strong>Feature #4</strong><span>Lorem ipsum dolor sit amet, ex paulo vidisse eos. Nec ut persius admodum civibus, an hinc iudico principes sea.</span></div></li>
    <li><svg width="20" height="20" viewBox="0 0 20 20"><circle cx="10" cy="10" r="9" fill="none" stroke="#e31e26" stroke-width="1.2"/><path d="M6 10.2 L9 13 L14.5 6.5" fill="none" stroke="#e31e26" stroke-width="1.2"/></svg><div><strong>Feature #5</strong><span>Lorem ipsum dolor sit amet, ex paulo vidisse eos. Nec ut persius admodum civibus, an hinc iudico principes sea.</span></div></li>
  </ul>
  <div class="footer">qtvlink.example | 10</div>
</section>

<!-- Closing slide -->
<section class="slide col-r row-4">
  <div class="closing-photo" role="img" aria-label="Soft, light office photograph behind the closing message"></div>
  <div class="closing-panel">
    <div class="closing-brand">QTVlink<i></i></div>
    <div class="thanks">THANK YOU</div>
    <div class="thanks-sub">FEEL FREE TO CONTACT US!</div>
    <div class="contact">
      <div><b>t:</b>+1 555 010 2040</div>
      <div><b>e:</b>hello@qtvlink.example</div>
      <div><b>w:</b>qtvlink.example</div>
    </div>
  </div>
  <div class="fine" style="text-align:center">Eu cum wisi tibens, eirmod neglegentur est te. Vix eros posse vocibus id, te est perpetua scriptorem.</div>
  <div class="sq red" style="left:307px;top:33px;width:39px;height:39px"></div>
  <div class="sq slate" style="left:369px;top:84px;width:48px;height:48px"></div>
  <div class="sq slate" style="left:278px;top:107px;width:57px;height:57px"></div>
  <div class="sq red" style="left:355px;top:162px;width:80px;height:80px"></div>
</section>

</body>
</html>
```